Visitenkarten-Design für Handwerksbetrieb mit Handel
Zielgruppe
Wir sind ein Handwerksbetrieb mit Handel (Haushaltsgeräte), Elektro,, Sicherheitstechnik, Heizung und Messtechnik (KRBS Messungen).
Aufgabenstellung
Bisheriges Layout, Styleguide

```html
<!DOCTYPE html>
<html lang="de">
<head>
<meta charset="utf-8">
<title>Visitenkarte BRENNER</title>
<link href="https://fonts.googleapis.com/css2?family=Nunito:wght@400;700;900&display=swap" rel="stylesheet">
<style>
  :root {
    --brand-red: #941a1c;
    --ink: #1a1a1a;
    --paper: #ffffff;
    --backdrop: #eff0f7;
  }
  * { margin: 0; padding: 0; box-sizing: border-box; }
  html, body {
    width: 1200px; height: 1200px; overflow: hidden;
    background: var(--backdrop);
    font-family: "Nunito", sans-serif;
  }
  .card {
    position: absolute; top: 469px;
    width: 419px; height: 271px;
  }
  .card--front { left: 179px; background: var(--brand-red); color: var(--paper); }
  .card--back { left: 630px; background: var(--paper); color: var(--ink); }

  .brand {
    position: absolute; top: 122px;
    font-weight: 900; font-size: 37px; line-height: 38px;
    letter-spacing: 0.5px;
  }
  .card--front .brand { right: 28px; color: var(--paper); }
  .card--back .brand { left: 20px; color: var(--ink); }

  .website {
    position: absolute; right: 27px; top: 228px;
    font-size: 13.5px; letter-spacing: 0.2px;
  }

  .contact { position: absolute; left: 219px; top: 38px; width: 200px; }
  .address { font-size: 13.5px; line-height: 17px; }
  .address + .address { margin-top: 10px; }
  .divider { height: 1px; background: var(--brand-red); margin-top: 17px; }
  .person { color: var(--brand-red); font-weight: 700; font-size: 13.5px; margin-top: 16px; }
  .phones { margin-top: 42px; list-style: none; }
  .phones li {
    display: flex; align-items: center; gap: 8px;
    font-size: 13.5px; line-height: 17px; letter-spacing: 0.3px;
  }
  .phones svg { width: 11px; height: 11px; flex: none; }
</style>
</head>
<body>
  <section class="card card--front">
    <p class="brand">BRENNER</p>
    <p class="website">brenner-elektro.de</p>
  </section>

  <section class="card card--back">
    <p class="brand">BRENNER</p>
    <div class="contact">
      <p class="address">Lindenweg 5<br>33100 Musterstadt</p>
      <p class="address">Marktstraße 12<br>33200 Beispielhof</p>
      <div class="divider"></div>
      <p class="person">Lukas Brenner</p>
      <ul class="phones">
        <li>
          <svg viewBox="0 0 12 12" aria-label="Telefon"><circle cx="6" cy="6" r="6" fill="#941a1c"/><path d="M4 3.2l1 1.3-.6.7c.4.8 1 1.4 1.8 1.8l.7-.6 1.3 1-.6 1C5.6 8.3 3.7 6.4 3.1 3.8z" fill="#fff"/></svg>
          01234 56 78 90
        </li>
        <li>
          <svg viewBox="0 0 12 12" aria-label="Fax"><circle cx="6" cy="6" r="6" fill="#941a1c"/><rect x="4.2" y="2.8" width="3.6" height="2.4" fill="#fff"/><rect x="3.2" y="5.6" width="5.6" height="2.6" rx=".5" fill="#fff"/><rect x="4.2" y="7.6" width="3.6" height="1.4" fill="#fff"/></svg>
          01234 56 78 901
        </li>
      </ul>
    </div>
  </section>
</body>
</html>
```